TBrenwick Business Cards & Letterhead

I have a logo but need a design for some new business cards. We are a Design-Build Firm that specializes in the design and construction of commercial projects.
the cards need to be professional. no cartoon stuff.
i would like to have the cards in AI format so I can update the card as needed. Logo is provided.
Our Address is: 4718 Fenmoor Ct. Brayton, South Carolina 29384

```html
<!DOCTYPE html>
<html lang="en">
<head>
<meta charset="utf-8">
<title>TBrenwick Business Card</title>
<link rel="stylesheet" href="https://fonts.googleapis.com/css2?family=Roboto:wght@400;500;700&display=swap">
<style>
  :root {
    --page: #e6e6e6;
    --card-white: #f6f6f7;
    --ink: #222222;
    --ink-soft: #444444;
    --brand-blue: #0b4a7a;
    --back-light: #0874a8;
    --back-mid: #035a8b;
    --back-dark: #023a63;
    --back-mark: #02365c;
  }
  * { box-sizing: border-box; margin: 0; padding: 0; }
  html, body {
    width: 1200px; height: 1200px; overflow: hidden;
    background: var(--page);
    font-family: "Roboto", Arial, sans-serif;
  }
  .canvas { position: relative; width: 1200px; height: 1200px; }
  .card {
    position: absolute; left: 257px; width: 686px; height: 392px;
    border-radius: 22px; overflow: hidden;
  }
  .card-front { top: 165px; background: var(--card-white); color: var(--ink); }
  .card-back {
    top: 653px;
    background: radial-gradient(ellipse 60% 65% at 50% 32%, var(--back-light) 0%, var(--back-mid) 55%, var(--back-dark) 100%);
  }
  .phones { position: absolute; left: 46px; top: 37px; font-size: 17px; line-height: 22px; }
  .phone-line { display: flex; align-items: center; gap: 10px; }
  .phone-line svg { width: 13px; height: 16px; fill: var(--brand-blue); }
  .person { position: absolute; left: 46px; top: 137px; }
  .person-name { font-size: 26px; font-weight: 700; color: #333; line-height: 30px; }
  .person-title { font-size: 17px; color: var(--ink-soft); margin-left: 2px; line-height: 22px; }
  .rule { position: absolute; left: 47px; top: 195px; width: 593px; height: 1px; background: #333; }
  .email { position: absolute; left: 46px; top: 203px; font-size: 17px; }
  .brand {
    position: absolute; right: 47px; top: 150px;
    display: flex; align-items: center; gap: 6px;
  }
  .brand-square { width: 30px; height: 30px; background: var(--brand-blue); }
  .brand-name { font-size: 38px; font-weight: 700; color: #3a3a3a; letter-spacing: -0.5px; line-height: 40px; }
  .address { position: absolute; left: 46px; top: 315px; font-size: 17px; line-height: 22px; }
  .website {
    position: absolute; right: 47px; top: 337px;
    font-size: 16px; font-weight: 700; letter-spacing: 3.4px; color: var(--brand-blue);
  }
  .back-brand {
    position: absolute; left: 0; right: 0; top: 168px;
    display: flex; justify-content: center; align-items: center; gap: 10px;
  }
  .back-brand .brand-square { width: 46px; height: 46px; background: var(--back-mark); }
  .back-brand .brand-name { font-size: 60px; line-height: 60px; color: var(--back-mark); }
</style>
</head>
<body>
<div class="canvas">
  <section class="card card-front">
    <div class="phones">
      <div class="phone-line">
        <svg viewBox="0 0 13 16" aria-hidden="true"><path d="M2 1 L5 1 L6 5 L4 6.5 Q6 10 8.5 12 L10 10 L13 11.5 L12.5 15 Q5 15 1 4 Z"/></svg>
        <span>(693) 5120-4418</span>
      </div>
      <div class="phone-line">
        <svg viewBox="0 0 13 16" aria-hidden="true"><path d="M2 0 H11 Q12 0 12 1 V15 Q12 16 11 16 H2 Q1 16 1 15 V1 Q1 0 2 0 Z M3 2 V12 H10 V2 Z"/></svg>
        <span>(693) 5120-4419</span>
      </div>
    </div>
    <div class="person">
      <div class="person-name">Aaron Whitfield</div>
      <div class="person-title">President</div>
    </div>
    <div class="brand">
      <span class="brand-square"></span>
      <span class="brand-name">TBRENWICK</span>
    </div>
    <div class="rule"></div>
    <div class="email">name@TBRENWICK.com</div>
    <div class="address">4718 Fenmoor Ct. Brayton<br>South Carolina 29384</div>
    <div class="website">www.TBRENWICK.com</div>
  </section>
  <section class="card card-back">
    <div class="back-brand">
      <span class="brand-square"></span>
      <span class="brand-name">TBRENWICK</span>
    </div>
  </section>
</div>
</body>
</html>
```